Talvin Crestline Homes needs a business card

We need a business card for a new company in Canada, Ontario. Our company is all about luxury contraction homes for our clients. Our product and services are custom projects design. Under the business logo that will be created, we want a slogan that will be a memorable phrase for consumers to remember us to tell their friends and relatives.

Additional infomation
- Brennick Solvadeu
- President / Ceo
-415.390.7628

Find point what luxury construction products and services can be done

We like to see colors:
- #663300
- and something other colors or color that would attract the client needs and wants

The final design should communicate leads from new or old clients that will grow our empire. Most of all, we try to work among the budget that clients want

NOTE
- we also need an icon for the business (Example: Pictoloop, Friendvane, and Chattorq icons)
- We want the company name to be remembered easily for clients and our distributors who would get our orders.
- we need an icon on the business cards: Friendvane and Pictoloop.

Thanks,
Talvin Crestline Homes

```html
<!DOCTYPE html>
<html lang="en">
<head>
<meta charset="utf-8">
<title>Talvin Crestline Homes – Business Card</title>
<link rel="stylesheet" href="https://fonts.googleapis.com/css2?family=Poppins:wght@400;500;600;800&display=swap">
<style>
  :root {
    --brown: #663300;
    --white: #ffffff;
    --ink: #0d0d0d;
    --band-text: #f1dcc6;
    --backdrop: #e9e4de;
  }
  * { margin: 0; padding: 0; box-sizing: border-box; }
  html, body {
    width: 1200px;
    height: 1156px;
    overflow: hidden;
    background: var(--backdrop);
  }
  .stage {
    position: relative;
    width: 1200px;
    height: 1156px;
  }
  .card {
    position: absolute;
    left: 200px;
    width: 800px;
    height: 457px;
    overflow: hidden;
    box-shadow: 0 6px 18px rgba(0,0,0,0.12);
  }

  /* Front: personal details */
  .card-front {
    top: 90px;
    background: var(--white);
  }
  .holder-name {
    position: absolute;
    left: 56px;
    top: 92px;
    font-family: "Poppins", sans-serif;
    font-weight: 800;
    font-size: 46px;
    line-height: 0.98;
    letter-spacing: 0.5px;
    color: var(--ink);
    text-transform: uppercase;
    z-index: 2;
  }
  .title-band {
    position: absolute;
    left: 0;
    right: 0;
    top: 176px;
    height: 52px;
    background: var(--brown);
    z-index: 1;
  }
  .holder-role {
    position: absolute;
    left: 56px;
    top: 196px;
    font-family: "Poppins", sans-serif;
    font-weight: 500;
    font-size: 18px;
    line-height: 1.2;
    letter-spacing: 0.5px;
    color: var(--band-text);
    z-index: 3;
  }
  .contact-phone {
    position: absolute;
    left: 56px;
    top: 240px;
    display: flex;
    align-items: center;
    gap: 12px;
    font-family: "Poppins", sans-serif;
    font-weight: 500;
    font-size: 17px;
    letter-spacing: 0.6px;
    color: var(--ink);
  }
  .contact-phone svg { width: 14px; height: 14px; fill: var(--brown); }
  .social-list {
    position: absolute;
    right: 36px;
    bottom: 56px;
    display: flex;
    gap: 14px;
    list-style: none;
    font-family: "Poppins", sans-serif;
    font-weight: 600;
    font-size: 12px;
    color: var(--brown);
  }
  .social-item { display: flex; align-items: center; gap: 5px; }
  .social-item::before {
    content: "";
    width: 9px;
    height: 9px;
    background: var(--brown);
    border-radius: 2px;
  }

  /* Back: company name */
  .card-back {
    top: 607px;
    background: var(--brown);
    display: flex;
    flex-direction: column;
    align-items: center;
    justify-content: center;
    color: var(--white);
    text-align: center;
  }
  .company-name {
    font-family: "Poppins", sans-serif;
    font-weight: 800;
    font-size: 50px;
    line-height: 1.1;
    letter-spacing: 0.5px;
    color: var(--white);
  }
  .company-tagline {
    margin-top: 8px;
    font-family: "Poppins", sans-serif;
    font-weight: 500;
    font-size: 19px;
    letter-spacing: 1.6px;
    text-transform: uppercase;
  }
</style>
</head>
<body>
<main class="stage">
  <section class="card card-front" aria-label="Business card front">
    <h1 class="holder-name">Brennick<br>Solvadeu</h1>
    <div class="title-band"></div>
    <p class="holder-role">President / Ceo</p>
    <p class="contact-phone">
      <svg viewBox="0 0 24 24" aria-hidden="true"><path d="M6.6 10.8a15.2 15.2 0 0 0 6.6 6.6l2.2-2.2a1 1 0 0 1 1-.25 11.4 11.4 0 0 0 3.6.57 1 1 0 0 1 1 1V20a1 1 0 0 1-1 1A17 17 0 0 1 3 4a1 1 0 0 1 1-1h3.5a1 1 0 0 1 1 1c0 1.25.2 2.45.57 3.57a1 1 0 0 1-.25 1z"/></svg>
      415-390-7628
    </p>
    <ul class="social-list">
      <li class="social-item">Friendvane</li>
      <li class="social-item">Pictoloop</li>
      <li class="social-item">Chattorq</li>
    </ul>
  </section>

  <section class="card card-back" aria-label="Business card back">
    <h2 class="company-name">Talvin Crestline Homes</h2>
    <p class="company-tagline">- Home Renovations - Custom Project Design -</p>
  </section>
</main>
</body>
</html>
```